Aerial photo/video drone company needs new business card

Aerial visual company who offers photos and video services via drones.

We are QVL certified and work in the real estate, insurance, construction, and film industries.

I'm looking for a clean, professional, maybe even edgy design, that will be a conversation starter when networking.

I've included our logo, current business card, and font.

Our current business card is decent; albeit, I'm looking for something more unique. If you folks provide good designs, I'll definitely guarantee payment (and I'm not opposed to tipping if the design is above and beyond).

Target Market(s)

Insurance companies, real estate agents, construction companies, advertising & other creative agencies, and filmmakers/producers.

Industry/Entity Type

Business

Contact Information for Business Card

Company name pronounced air-a-vee.

Font styles to use
Other font styles liked:
• Font was uploaded; that or similar; not opposed to other fonts if they work well with the design

Requirements
Must have
• Clearly prominent logo; my name and title; phone number; email address; web address; mentioned "QVL Certified" or similar; should indicate "Aerial visual"
Nice to have
• Watermark of logo or otherwise
Should not have
• Pictures of drones or scenic shots

```html
<!DOCTYPE html>
<html lang="en">
<head>
<meta charset="utf-8">
<title>Skyvant Business Card</title>
<link href="https://fonts.googleapis.com/css2?family=Montserrat:wght@500;600;700&display=swap" rel="stylesheet">
<style>
  :root {
    --navy: #2b3a5c;
    --sky: #4a8fd6;
    --card: #e5e5e7;
    --backdrop: #f1f1ef;
  }
  * { margin: 0; padding: 0; box-sizing: border-box; }
  html, body { width: 1200px; height: 842px; overflow: hidden; }
  body {
    background: var(--backdrop);
    font-family: "Montserrat", sans-serif;
    position: relative;
  }
  .card {
    position: absolute;
    top: 266px;
    width: 540px;
    height: 310px;
    background: var(--card);
    overflow: hidden;
    box-shadow: 0 2px 10px rgba(0,0,0,0.12);
  }
  .card--front { left: 40px; }
  .card--back { left: 620px; }

  .card__band-accent {
    position: absolute; left: 0; right: 0; bottom: 50px; height: 8px;
    background: var(--sky);
  }
  .card__band-base {
    position: absolute; left: 0; right: 0; bottom: 0; height: 50px;
    background: var(--navy);
  }

  /* Front */
  .front__brand {
    position: absolute; left: 0; right: 0; top: 82px;
    display: flex; flex-direction: column; align-items: center;
  }
  .front__name-row { display: flex; align-items: center; gap: 14px; }
  .brand-dot { width: 22px; height: 22px; border-radius: 50%; background: var(--navy); }
  .front__wordmark {
    font-size: 74px; font-weight: 700; color: var(--navy);
    letter-spacing: 1px; line-height: 1;
  }
  .front__cert {
    margin-top: 8px; font-size: 14px; font-weight: 600;
    color: var(--navy); letter-spacing: 5px;
  }

  /* Back */
  .back__brand {
    position: absolute; right: 34px; top: 28px;
    display: flex; flex-direction: column; align-items: flex-end;
  }
  .back__name-row { display: flex; align-items: center; gap: 7px; }
  .back__brand .brand-dot { width: 11px; height: 11px; }
  .back__wordmark {
    font-size: 34px; font-weight: 700; color: var(--navy); line-height: 1;
  }
  .back__tagline {
    margin-top: 3px; font-size: 7.5px; font-weight: 600; color: var(--sky);
    text-align: right; line-height: 1.45;
  }
  .back__person { position: absolute; left: 34px; top: 160px; }
  .back__person-name {
    font-size: 16px; font-weight: 700; color: var(--navy); letter-spacing: 0.3px;
  }
  .back__person-role {
    font-size: 9px; font-weight: 600; color: var(--sky); margin-top: 1px;
  }
  .contact-rule {
    position: absolute; left: 24px; right: 24px; top: 205px; height: 2px;
    background: var(--navy);
  }
  .contact {
    position: absolute; top: 195px;
    display: flex; flex-direction: column; align-items: center;
  }
  .contact__icon {
    width: 22px; height: 22px; border-radius: 50%; background: var(--navy);
    display: flex; align-items: center; justify-content: center;
  }
  .contact__text {
    margin-top: 5px; font-size: 13px; font-weight: 600; color: var(--sky);
    white-space: nowrap;
  }
  .contact--email { left: 46px; }
  .contact--phone { left: 232px; }
  .contact--web { right: 44px; align-items: flex-end; }
  .contact--web .contact__icon { margin-right: 18px; }
  .contact--email { align-items: flex-start; }
  .contact--email .contact__icon { margin-left: 40px; }
</style>
</head>
<body>
  <section class="card card--front" aria-label="Card front">
    <div class="front__brand">
      <div class="front__name-row">
        <span class="brand-dot"></span>
        <span class="front__wordmark">skyvant</span>
      </div>
      <span class="front__cert">QVL CERTIFIED</span>
    </div>
    <div class="card__band-accent"></div>
    <div class="card__band-base"></div>
  </section>

  <section class="card card--back" aria-label="Card back">
    <div class="back__brand">
      <div class="back__name-row">
        <span class="brand-dot"></span>
        <span class="back__wordmark">skyvant</span>
      </div>
      <p class="back__tagline">QVL Part 107 Commercial sUAS Certified<br>Aerial Visual for Real Estate | Insurance | Construction | Film</p>
    </div>

    <div class="back__person">
      <p class="back__person-name">DANIEL J. MORROW</p>
      <p class="back__person-role">Owner | sUAS Pilot</p>
    </div>

    <div class="contact-rule"></div>

    <div class="contact contact--email">
      <span class="contact__icon">
        <svg width="12" height="9" viewBox="0 0 12 9"><rect x="0.5" y="0.5" width="11" height="8" fill="none" stroke="#fff"/><path d="M0.5 0.5 L6 5 L11.5 0.5" fill="none" stroke="#fff"/></svg>
      </span>
      <span class="contact__text">dan@skyvant.com</span>
    </div>

    <div class="contact contact--phone">
      <span class="contact__icon">
        <svg width="12" height="11" viewBox="0 0 12 11"><path d="M1 3 Q6 -1 11 3 L9.5 4.5 L8 3.5 L8 2.5 Q6 1.8 4 2.5 L4 3.5 L2.5 4.5 Z" fill="#fff"/><rect x="2.5" y="5" width="7" height="5" rx="1" fill="#fff"/></svg>
      </span>
      <span class="contact__text">555.014.2290</span>
    </div>

    <div class="contact contact--web">
      <span class="contact__icon">
        <svg width="12" height="12" viewBox="0 0 12 12" fill="none" stroke="#fff" stroke-width="1"><circle cx="6" cy="6" r="5"/><ellipse cx="6" cy="6" rx="2.2" ry="5"/><path d="M1 6 H11 M2 3.5 H10 M2 8.5 H10"/></svg>
      </span>
      <span class="contact__text">skyvant.com</span>
    </div>

    <div class="card__band-accent"></div>
    <div class="card__band-base"></div>
  </section>
</body>
</html>
```